Postcard Design

Name of the Company is : Harbor Lantern Sport Fishing Charters Block Island RI
Name of the boat : Reel Tide Joy
local Captain Dennis Hartwell
pricing and booking : 401-555-0193
We specialize in:

Shark & Tuna Trips
Full or half day Inshore Bass & Bluefish
Half day bottom fishing for Fluke, Sea Bass & Scup
Inshore night fishing trips
Custom Combination Charters also available
Our crew provides:
A professional and accommodating experience
A very child friendly environment
A range of technique options for every style of trip
An immense knowledge of the waters.
Our Vessel:
Meets all NMSA safety requirement
Twin 250 Hp Valdrek Turbo Diesels
All updated electronics
On the comfort side : we have a restroom, and a galley area with a table so you can enjoy your lunch.

Payments : We except; Cash , Check , Kp, Tz, Rl and Nb

I have attached the logo I would like to use . If possible I would like to use the banners on the logo with Company Name & number.

```html
<!DOCTYPE html>
<html lang="en">
<head>
<meta charset="utf-8">
<title>Harbor Lantern Sport Fishing Charters – Postcard</title>
<link href="https://fonts.googleapis.com/css2?family=Roboto+Condensed:wght@300;400&family=Roboto:wght@700&family=Source+Sans+3:wght@700&family=Dancing+Script:wght@500&display=swap" rel="stylesheet">
<style>
  :root {
    --sky-top: #ffffff;
    --sky-mid: #d6ebf8;
    --sky-bottom: #a6d2ef;
    --navy: #24487f;
    --ink: #222a33;
    --list-ink: #2b3f6b;
    --divider: #7f9fb8;
  }
  * { margin: 0; padding: 0; box-sizing: border-box; }
  html, body { width: 1200px; height: 930px; overflow: hidden; }
  body { background: var(--sky-top); }

  .postcard {
    position: relative;
    width: 1200px;
    height: 930px;
    overflow: hidden;
    background: linear-gradient(180deg, var(--sky-top) 0%, var(--sky-mid) 45%, var(--sky-bottom) 100%);
    font-family: "Roboto Condensed", "Arial Narrow", sans-serif;
  }

  /* Brand block */
  .brand {
    position: absolute;
    left: 300px;
    top: 90px;
    width: 600px;
    text-align: center;
    color: var(--navy);
  }
  .brand-name {
    font-family: "Source Sans 3", "Helvetica Neue", sans-serif;
    font-weight: 700;
    font-size: 50px;
    line-height: 1.15;
  }
  .brand-phone {
    margin-top: 40px;
    font-family: "Source Sans 3", "Helvetica Neue", sans-serif;
    font-weight: 700;
    font-size: 44px;
  }

  /* Booking column */
  .booking {
    position: absolute;
    left: 60px;
    top: 500px;
    width: 474px;
    text-align: center;
  }
  .booking-lead {
    font-size: 28px;
    font-weight: 400;
    color: var(--ink);
  }
  .booking-phone {
    font-family: "Roboto", Arial, sans-serif;
    font-weight: 700;
    font-size: 53px;
    color: var(--navy);
    line-height: 1.1;
  }
  .payment-lead {
    margin-top: 26px;
    font-size: 28px;
    color: var(--ink);
  }
  .payment-list {
    list-style: none;
    display: flex;
    justify-content: center;
    gap: 52px;
    margin-top: 22px;
  }
  .payment-list li {
    font-size: 30px;
    font-weight: 400;
    color: var(--navy);
    width: 52px;
  }

  .divider {
    position: absolute;
    left: 546px;
    top: 462px;
    width: 4px;
    height: 330px;
    background: linear-gradient(180deg, rgba(127,159,184,0) 0%, var(--divider) 50%, rgba(127,159,184,0) 100%);
  }

  /* Vessel features */
  .features {
    position: absolute;
    left: 578px;
    top: 478px;
    width: 580px;
    list-style: none;
    color: var(--list-ink);
    font-size: 30px;
    font-weight: 300;
    line-height: 39px;
  }
  .features li {
    position: relative;
    padding-left: 28px;
  }
  .features li.spaced { margin-top: 39px; }
  .features svg {
    position: absolute;
    left: 0;
    top: 12px;
    width: 16px;
    height: 16px;
  }

  .tagline {
    position: absolute;
    left: 0;
    top: 818px;
    width: 1200px;
    text-align: center;
    font-family: "Dancing Script", cursive;
    font-weight: 500;
    font-size: 52px;
    color: var(--navy);
  }
</style>
</head>
<body>
<main class="postcard">
  <header class="brand">
    <h1 class="brand-name">Harbor Lantern<br>Sport Fishing Charters</h1>
    <p class="brand-phone">(401) 555-0193</p>
  </header>

  <section class="booking">
    <p class="booking-lead">Book your experience today!</p>
    <p class="booking-phone">(401) 555-0193</p>
    <p class="payment-lead">Cash &amp; Checks</p>
    <ul class="payment-list">
      <li>Kp</li>
      <li>Rl</li>
      <li>Tz</li>
      <li>Nb</li>
    </ul>
  </section>

  <div class="divider"></div>

  <ul class="features">
    <li><svg viewBox="0 0 16 16"><path d="M2 3 L14 8 L2 13 L5 8 Z" fill="#2b3f6b"/></svg>Our vessel meets all NMSA safety<br>requirements</li>
    <li><svg viewBox="0 0 16 16"><path d="M2 3 L14 8 L2 13 L5 8 Z" fill="#2b3f6b"/></svg>Twin 250 Hp Valdrek Turbo Diesels</li>
    <li><svg viewBox="0 0 16 16"><path d="M2 3 L14 8 L2 13 L5 8 Z" fill="#2b3f6b"/></svg>All updated electronics</li>
    <li class="spaced"><svg viewBox="0 0 16 16"><path d="M2 3 L14 8 L2 13 L5 8 Z" fill="#2b3f6b"/></svg>We have a restroom and a galley area<br>with a table so you can enjoy your lunch!</li>
  </ul>

  <p class="tagline">A bad day fishing is better than a good day at work!</p>
</main>
</body>
</html>
```